Personal Motivational Quote Poster Design

I would like to create a poster with some of my favorite quotes to hang in my office. I did similar projects in 2012 and 2014. I've uploaded the winning designs so you can get a better idea of what I'm looking for. I will provide feedback on your design within 24 hours of receiving it.

The poster must contain the following quotes:

“What the pupil must learn, if he learns anything at all, is that the world will do most of the work for you, provided you cooperate with it by identifying how it really works and aligning with those realities. If we do not let the world teach us, it teaches us a lesson.” - Walter Brindley

“I tackle every big new problem by asking two questions: Who has dealt with this problem well? And what can we learn from them?” - Hal Porter

“If we can really understand the problem, the answer will come out of it, because the answer is not separate from the problem.” - Ravel Ondashanti

“Success is nothing more than a few simple disciplines, practiced every day; while failure is simply a few errors in judgment, repeated every day. It is the accumulative weight of our disciplines and our judgments that leads us to either fortune or failure.” - Ned Calve

“Inaction breeds doubt and fear. Action breeds confidence and courage.” - Rex Halloway

“What’s the one thing you can do, such that by doing it, everything else will be easier or unnecessary?” - Lyle Danvers

Requirements
Must have
• The poster will be 24" high x 36" long and printed on canvas, so the image you create needs to have a resolution of at least 2700 x 3900.
Nice to have
• I don't have an exact vision for how the poster should look, so I am totally open to you using your creativity to develop, arrange and present the content as you'd like.

That said, I would like an image (photo or posterized image) of the person being quoted along with each quote. I do not have specific images that I would like you to use, so you will need to find the images on your own.

The images don't need to be perfect... I am more interested in the poster relating the essence of the quotes and the people being quoted than I am in perfect photographic images of the people being quoted.

```html
<!DOCTYPE html>
<html lang="en">
<head>
<meta charset="utf-8">
<title>Favourite Quotes Poster</title>
<link rel="stylesheet" href="https://fonts.googleapis.com/css2?family=Delius&family=Caveat:wght@400&display=swap">
<style>
  :root{
    --ink:#111111;
    --paper:#ffffff;
    --apricot:#fbae5c;
    --apricot-shade:#d98c4a;
    --teal:#7ecfc9;
    --teal-shade:#5aa9a4;
    --violet:#635caa;
    --violet-shade:#4b4588;
    --tangerine:#f26722;
    --tangerine-shade:#c9562a;
    --raspberry:#cc2a5e;
    --raspberry-shade:#a8234f;
    --cornflower:#7ba7d9;
    --cornflower-shade:#5a7fae;
    --tan-edge:#c8a070;
    --quote-font:"Delius", "Trebuchet MS", sans-serif;
    --name-font:"Caveat", "Comic Sans MS", cursive;
  }
  *{margin:0;padding:0;box-sizing:border-box;}
  html,body{width:1200px;height:800px;overflow:hidden;background:var(--ink);}
  .poster{position:relative;width:1200px;height:800px;background:var(--ink);color:var(--paper);font-family:var(--quote-font);}
  .poster__shapes{position:absolute;inset:0;}
  .quote{position:absolute;}
  .quote__line{position:absolute;left:0;right:0;white-space:nowrap;line-height:1;}
  .quote__line--spread{display:flex;justify-content:space-between;align-items:baseline;}
  .quote__line--right{text-align:right;}
  .author{position:absolute;font-family:var(--name-font);font-size:22px;line-height:1;white-space:nowrap;color:var(--paper);}
  .author--right{text-align:right;}
  .open-mark{position:absolute;left:52px;top:44px;font-size:34px;font-style:italic;line-height:1;}

  .s-body{font-size:20px;}
  .s-mid{font-size:26px;}
  .s-big{font-size:30px;}
  .s-xl{font-size:30px;}
  .s-small{font-size:17px;}

  .quote--pupil{left:49px;width:525px;top:0;height:300px;}
  .quote--courage{left:620px;width:510px;top:0;height:240px;}
  .quote--success{left:643px;width:502px;top:0;height:520px;}
  .quote--tackle{left:52px;width:520px;top:0;height:520px;}
  .quote--separate{left:52px;width:525px;top:0;height:740px;}
  .quote--onething{left:641px;width:503px;top:0;height:740px;}
</style>
</head>
<body>
<main class="poster">
  <svg class="poster__shapes" width="1200" height="800" viewBox="0 0 1200 800">
    <defs>
      <linearGradient id="fade-apricot" x1="0" y1="0" x2="0" y2="1"><stop offset="0" stop-color="#d98c4a" stop-opacity=".35"/><stop offset="1" stop-color="#d98c4a" stop-opacity=".9"/></linearGradient>
      <linearGradient id="fade-teal" x1="0" y1="0" x2="0" y2="1"><stop offset="0" stop-color="#5aa9a4" stop-opacity=".3"/><stop offset="1" stop-color="#5aa9a4" stop-opacity=".85"/></linearGradient>
      <linearGradient id="fade-violet" x1="0" y1="0" x2="0" y2="1"><stop offset="0" stop-color="#4b4588" stop-opacity=".3"/><stop offset="1" stop-color="#4b4588" stop-opacity=".9"/></linearGradient>
      <linearGradient id="fade-tangerine" x1="0" y1="0" x2="0" y2="1"><stop offset="0" stop-color="#c9562a" stop-opacity=".35"/><stop offset="1" stop-color="#c9562a" stop-opacity=".9"/></linearGradient>
      <linearGradient id="fade-raspberry" x1="0" y1="0" x2="0" y2="1"><stop offset="0" stop-color="#a8234f" stop-opacity=".3"/><stop offset="1" stop-color="#e07a9a" stop-opacity=".7"/></linearGradient>
      <linearGradient id="fade-cornflower" x1="0" y1="0" x2="0" y2="1"><stop offset="0" stop-color="#5a7fae" stop-opacity=".3"/><stop offset="1" stop-color="#2e3f5c" stop-opacity=".8"/></linearGradient>
    </defs>

    <rect class="panel panel--apricot" x="22" y="51" width="584" height="250" fill="var(--apricot)"/>
    <rect class="portrait" x="444" y="158" width="143" height="148" rx="40" fill="url(#fade-apricot)" role="img" aria-label="Tinted portrait photo of Walter Brindley"/>
    <polygon class="frame" points="33,37 606,48 601,296 29,286" fill="none" stroke="var(--paper)" stroke-width="2.5"/>

    <polygon class="panel panel--teal" points="610,43 1169,17 1179,231 621,255" fill="var(--teal)"/>
    <rect class="portrait" x="633" y="97" width="143" height="140" rx="40" fill="url(#fade-teal)" role="img" aria-label="Tinted portrait photo of Rex Halloway"/>
    <rect class="frame" x="620" y="34" width="545" height="203" fill="none" stroke="var(--paper)" stroke-width="2.5"/>

    <polygon class="panel panel--violet" points="606,255 1180,267 1177,513 612,502" fill="var(--violet)"/>
    <rect class="portrait" x="985" y="423" width="158" height="97" rx="30" fill="url(#fade-violet)" role="img" aria-label="Tinted portrait photo of Ned Calve speaking"/>
    <rect class="frame" x="618" y="257" width="545" height="263" fill="none" stroke="var(--paper)" stroke-width="2.5"/>

    <polygon class="panel panel--tangerine" points="36,311 607,308 612,515 39,527" fill="var(--tangerine)" stroke="var(--tan-edge)" stroke-width="2"/>
    <rect class="portrait" x="117" y="378" width="179" height="130" rx="40" fill="url(#fade-tangerine)" role="img" aria-label="Tinted portrait photo of Hal Porter"/>
    <rect class="frame" x="34" y="321" width="575" height="188" fill="none" stroke="var(--paper)" stroke-width="2.5"/>

    <polygon class="panel panel--raspberry" points="20,542 600,531 601,736 26,749" fill="var(--raspberry)" stroke="var(--tan-edge)" stroke-width="2"/>
    <rect class="portrait" x="444" y="607" width="117" height="130" rx="35" fill="url(#fade-raspberry)" role="img" aria-label="Tinted portrait photo of Ravel Ondashanti"/>
    <rect class="frame" x="31" y="531" width="569" height="195" fill="none" stroke="var(--paper)" stroke-width="2.5"/>

    <polygon class="panel panel--cornflower" points="606,541 1171,529 1177,742 598,759" fill="var(--cornflower)"/>
    <rect class="portrait" x="643" y="612" width="138" height="136" rx="40" fill="url(#fade-cornflower)" role="img" aria-label="Tinted portrait photo of Lyle Danvers smiling"/>
    <polygon class="frame" points="607,541 1172,530 1176,741 612,753" fill="none" stroke="var(--paper)" stroke-width="2.5"/>
  </svg>

  <span class="open-mark">"</span>
  <section class="quote quote--pupil">
    <div class="quote__line quote__line--spread s-body" style="top:75px;padding-left:30px;"><span>What</span><span>the</span><span>pupil</span><span>must</span><span>learn,</span><span>if</span><span>he</span><span>learns</span><span>anything</span><span>at</span></div>
    <div class="quote__line quote__line--spread s-body" style="top:102px;"><span>all,</span><span>is</span><span>that</span><span>the</span><span>world</span><span>will</span><span>do</span><span>most</span><span>of</span><span>the</span><span>work</span><span>for</span><span>you,</span></div>
    <div class="quote__line quote__line--spread s-body" style="top:129px;"><span>provided</span><span>you</span><span>cooperate</span><span>with</span><span>it</span><span>by</span><span>identifying</span><span>how</span><span>it</span></div>
    <div class="quote__line s-body" style="top:156px;">really works and aligning with those realities.</div>
    <div class="quote__line quote__line--spread s-xl" style="top:183px;padding-left:12px;"><span>If</span><span>we</span><span>do</span><span>not</span><span>let</span><span>the</span><span>world</span><span>teach</span><span>us,</span><span>it</span></div>
    <div class="quote__line s-xl" style="top:219px;">teaches us a lesson.”</div>
  </section>
  <p class="author" style="left:55px;top:258px;">-Walter Brindley</p>

  <section class="quote quote--courage">
    <div class="quote__line quote__line--right" style="top:76px;"><span class="s-xl">Inaction</span> <span class="s-small">breeds</span> <span class="s-big">doubt and fear.</span></div>
    <div class="quote__line" style="top:116px;left:24px;"><span class="s-xl">Action</span> <span class="s-small">breeds</span> <span class="s-big">confidence and courage.”</span></div>
  </section>
  <p class="author author--right" style="right:70px;top:206px;">- Rex Halloway</p>

  <section class="quote quote--success">
    <div class="quote__line quote__line--spread" style="top:270px;"><span class="s-big">“Success</span><span class="s-body">is</span><span class="s-body">nothing</span><span class="s-body">more</span><span class="s-body">than</span><span class="s-body">a</span><span class="s-body">few</span><span class="s-body">simple</span></div>
    <div class="quote__line quote__line--spread" style="top:307px;"><span class="s-body">disciplines,</span><span class="s-body">practiced</span><span class="s-body">every</span><span class="s-body">day;</span><span class="s-body">while</span><span class="s-big">failure</span><span class="s-body">is</span></div>
    <div class="quote__line quote__line--spread s-body" style="top:343px;"><span>simply</span><span>a</span><span>few</span><span>errors</span><span>in</span><span>judgment,</span><span>repeated</span><span>every</span><span>day.</span></div>
    <div class="quote__line quote__line--spread" style="top:369px;"><span class="s-body">It</span><span class="s-body">is</span><span class="s-body">the</span><span class="s-body">accumulative</span><span class="s-body">weight</span><span class="s-body">of</span><span class="s-mid">our</span><span class="s-mid">disciplines</span></div>
    <div class="quote__line quote__line--spread" style="top:402px;"><span class="s-mid">and</span><span class="s-mid">our</span><span class="s-mid">judgments</span><span class="s-body">that</span><span class="s-mid">leads</span><span class="s-mid">us</span><span class="s-mid">to</span><span class="s-mid">either</span></div>
    <div class="quote__line quote__line--right s-mid" style="top:436px;">fortune or failure.”</div>
  </section>
  <p class="author author--right" style="right:55px;top:497px;">-Ned Calve</p>

  <section class="quote quote--tackle">
    <div class="quote__line s-body" style="top:336px;">“I tackle every big new problem by asking two</div>
    <div class="quote__line" style="top:369px;"><span class="s-body">questions:</span> <span class="s-big">Who</span> <span class="s-body">has dealt with this problem well?</span></div>
    <div class="quote__line" style="top:409px;"><span class="s-body">And</span> <span class="s-big">what</span> <span class="s-body">can we learn from them?”</span></div>
  </section>
  <p class="author" style="left:58px;top:470px;">- Hal Porter</p>

  <section class="quote quote--separate">
    <div class="quote__line quote__line--spread s-body" style="top:548px;"><span>“If</span><span>we</span><span>can</span><span>really</span><span>understand</span><span>the</span><span>problem,</span><span>the</span><span>answer</span></div>
    <div class="quote__line" style="top:580px;"><span class="s-body">will come out of it, because</span> <span class="s-xl">the answer is not</span></div>
    <div class="quote__line s-xl" style="top:619px;">separate from the problem.”</div>
  </section>
  <p class="author" style="left:58px;top:682px;">-Ravel Ondashanti</p>

  <section class="quote quote--onething">
    <div class="quote__line quote__line--spread" style="top:568px;"><span class="s-body">“What’s</span><span class="s-big">the</span><span class="s-big">one</span><span class="s-big">thing</span><span class="s-big">you</span><span class="s-big">can</span><span class="s-big">do,</span></div>
    <div class="quote__line quote__line--spread s-body" style="top:603px;"><span>such</span><span>that</span><span>by</span><span>doing</span><span>it,</span><span>everything</span><span>else</span><span>will</span><span>be</span><span>easier</span></div>
    <div class="quote__line quote__line--right s-body" style="top:630px;">or unnecessary?”</div>
  </section>
  <p class="author author--right" style="right:56px;top:684px;">- Lyle Danvers</p>
</main>
</body>
</html>
```